Qorvane Industries needs an A4 flyer (2 sides)

Qorvane Industries is an Australian Owned and Operated business offering 1) metallurgical consulting service and 2) tooling supplier to Australia's manufacturing industry. The purpose of this flyer is to portray the business to its audience as an 'Japanese Quality' Tool Supplier backed by a metallurgical expert, who knows what it takes to manufacture high performance precision tools. With over 20 years experience as a metallurgist, i have come across hundreds of problems (failures) related to steel and tools that prompted me to start a tool making business. Making tools that out last ordinary tools. Our tools are of superior quality, performance and price competitive to Australian made tools because they are made by a Japanese Owned Tool making company, who supplies Japan. All our tools are made with Only Japanese Tool Steel from well known brands such as Kerova, Belmu, Torunami. Our products include: Extrusion Die, Stamping Die, Forming Die, Forging Die, Customised Tools and Components.
The purpose of the flyer is catch attention of the production manager, engineering manager and tooling manager as "Why should i consider doing business with you?", why should i trust your tools?

Target Market(s)

Australian manufacturers associating with Aluminium Extrusion, Metal Products, Plastic extrusion, PVC extrusion and Sheet Metal Industry

Industry/Entity Type

Metal Stamping

Font styles to use
Sans Serif

Colors

Designer to choose colors to be used in the design.

Requirements
Must have
• Australian Owned & Operated (front page)
Genuine Japanese Quality (Tools & Dies)
Japanese Tool Steel
Kerova, Belmu, Torunami (Steels)
Nice to have
• Please use photos provided and read existing brochure to get some depth and nature of the business and technical capacity. Any suggestion or request of photos is welcome, please email me.
Should not have
• Not sure at this stage

```html
<!DOCTYPE html>
<html lang="en">
<head>
<meta charset="utf-8">
<title>Qorvane Industries – Flyer</title>
<link rel="stylesheet" href="https://fonts.googleapis.com/css2?family=Oswald:wght@300;400;500;600;700&family=Montserrat:wght@400;500;600;700&display=swap">
<style>
  :root{
    --teal:#5c9ea5;
    --teal-dark:#4b8c94;
    --green:#8ca65a;
    --green-bright:#8fb04a;
    --ink:#2b2b2b;
    --grey-logo:#8d8f92;
    --canvas:#e4e5e8;
    --white:#ffffff;
  }
  *{box-sizing:border-box;margin:0;padding:0}
  html,body{width:750px;height:1200px;overflow:hidden}
  body{background:var(--canvas);position:relative;font-family:"Montserrat",sans-serif;color:var(--ink)}

  .sheet{position:absolute;left:175px;width:400px;height:565px;box-shadow:0 3px 10px rgba(0,0,0,.25);background:var(--white);overflow:hidden}
  .sheet--front{top:22px}
  .sheet--back{top:613px}
  .page{position:absolute;left:0;top:0;width:708px;height:1000px;transform:scale(.565);transform-origin:0 0;background:var(--white)}
  .abs{position:absolute}
  .nowrap{white-space:nowrap}
  .shapes{position:absolute;left:0;top:0;width:708px;height:1000px}

  /* front */
  .hero-photo{left:0;top:172px;width:708px;height:460px;
    background:radial-gradient(ellipse at 40% 55%,#c7c5bf 0%,#9d9d97 45%,#7b7d78 100%)}
  .brand-box{left:32px;top:0;width:278px;height:272px;background:var(--white);
    display:flex;flex-direction:column;justify-content:center;align-items:center}
  .brand-name{font-family:"Oswald",sans-serif;font-weight:700;color:var(--grey-logo);
    text-transform:uppercase;text-align:center;line-height:1.05}
  .brand-name .line1{display:block;font-size:62px;letter-spacing:2px}
  .brand-name .line2{display:block;font-size:36px;letter-spacing:1px}
  .website{right:28px;top:70px;display:flex;align-items:center;gap:12px;
    font-family:"Montserrat",sans-serif;font-weight:600;font-size:21px;color:var(--ink);white-space:nowrap}
  .ownership{right:28px;top:112px;font-family:"Montserrat",sans-serif;font-weight:700;font-size:14px;
    letter-spacing:.6px;color:var(--teal);white-space:nowrap}
  .headline{right:28px;top:250px;text-align:right;font-family:"Oswald",sans-serif;color:var(--white);text-transform:uppercase;white-space:nowrap}
  .headline .big{display:block;font-weight:700;font-size:54px;line-height:56px}
  .headline .mid{display:block;font-weight:600;font-size:33px;line-height:40px}
  .headline .light{display:block;font-weight:400;font-size:33px;line-height:39px}
  .quality{right:28px;top:588px;text-align:right;font-family:"Montserrat",sans-serif;font-weight:700;font-size:13px;
    line-height:17px;color:var(--white);letter-spacing:.4px;white-space:nowrap}

  .steel-title{left:30px;top:654px;width:296px;text-align:center;color:var(--white);font-family:"Oswald",sans-serif;white-space:nowrap}
  .steel-title h2{font-weight:600;font-size:26px;line-height:34px;letter-spacing:.3px}
  .steel-title p{font-weight:300;font-size:18px;line-height:26px;letter-spacing:.5px}
  .steel-badge{width:133px;height:46px;background:var(--white);display:flex;align-items:center;justify-content:center;gap:6px;
    font-family:"Montserrat",sans-serif;font-weight:700;font-size:12px;color:var(--ink);text-transform:uppercase;white-space:nowrap}
  .steel-badge .dot{width:9px;height:9px;background:var(--teal-dark)}
  .features{left:70px;top:854px;list-style:none;color:var(--white);font-size:14px;font-weight:500;white-space:nowrap}
  .features li{display:flex;align-items:center;gap:8px;height:29.7px}
  .features .ring{width:22px;height:22px;border:1.5px solid var(--white);border-radius:50%;flex:none}
  .benefits{left:428px;top:658px;list-style:none;font-size:14px;white-space:nowrap}
  .benefits li{display:flex;align-items:center;gap:8px;height:58px}
  .benefits b{font-weight:700}
  .benefits svg{flex:none}
  .company{left:392px;top:872px;width:300px;text-align:center;white-space:nowrap}
  .company h3{font-family:"Oswald",sans-serif;font-weight:600;font-size:30px;line-height:38px;color:var(--teal)}
  .company .division{font-size:11.5px;line-height:15px}
  .company .abn{font-size:13px;font-weight:600;margin-top:16px}

  /* back */
  .section-title{left:200px;top:32px;width:306px;height:44px;border-top:2px solid var(--teal);border-bottom:2px solid var(--teal);
    font-family:"Oswald",sans-serif;font-weight:600;font-size:29px;line-height:40px;color:var(--teal);text-align:center;white-space:nowrap}
  .service{top:110px;width:160px;text-align:center}
  .service h4{font-weight:700;font-size:15.5px;line-height:20px;color:var(--teal);text-transform:uppercase}
  .service p{font-size:13px;line-height:17px;color:var(--ink)}
  .divider{top:92px;width:1.5px;height:104px;background:var(--teal)}
  .feature-photo{left:0;top:220px;width:345px;height:392px;
    background:linear-gradient(180deg,#a7aaa6 0%,#8d918c 40%,#b4a98f 100%)}
  .caption{height:22px;background:var(--green-bright);color:var(--white);font-size:11px;font-weight:600;text-align:center;line-height:22px;white-space:nowrap}
  .caption--tall{left:0;top:565px;width:300px;height:36px;line-height:14px;padding-top:4px}
  .about{left:364px;top:264px;width:318px;color:var(--white)}
  .about h5{font-family:"Oswald",sans-serif;font-weight:600;font-size:20px;line-height:24px;text-transform:uppercase}
  .about p{font-size:13px;line-height:17px;margin-bottom:34px}
  .tile{width:318px;height:167px}
  .tile .fill{width:100%;height:145px}
  .tile .caption{width:100%}
</style>
</head>
<body>

<section class="sheet sheet--front" aria-label="Flyer front">
  <div class="page">
    <div class="abs hero-photo" role="img" aria-label="Close-up photo of a precision machined tool with coloured hoses"></div>
    <svg class="shapes" viewBox="0 0 708 1000" aria-hidden="true">
      <polygon points="490,172 708,172 708,632 400,632" fill="var(--green)" opacity=".93"/>
      <polygon points="0,632 400,632 330,1000 0,1000" fill="var(--teal)"/>
    </svg>

    <div class="abs brand-box">
      <div class="brand-name"><span class="line1">Qorvane</span><span class="line2">Industries</span></div>
    </div>

    <div class="abs website">
      <svg width="28" height="28" viewBox="0 0 28 28" aria-hidden="true">
        <circle cx="14" cy="14" r="12.5" fill="var(--teal)"/>
        <g fill="none" stroke="#fff" stroke-width="1.4">
          <ellipse cx="14" cy="14" rx="5" ry="12.5"/>
          <line x1="1.5" y1="14" x2="26.5" y2="14"/>
          <path d="M3.5 8h21M3.5 20h21"/>
        </g>
      </svg>
      WWW.QORVANE.COM.AU
    </div>
    <p class="abs ownership">AUSTRALIAN OWNED &amp; OPERATED</p>

    <h1 class="abs headline">
      <span class="big">Tooling</span>
      <span class="big">Design &amp;</span>
      <span class="mid">Manufacture</span>
      <span class="light">Specialist</span>
      <span class="light">Metallurgical</span>
      <span class="light">Solutions</span>
      <span class="light">Provider</span>
    </h1>
    <p class="abs quality">GENUINE JAPANESE QUALITY<br>TOOLS &amp; DIES</p>

    <div class="abs steel-title">
      <h2>TOOL CHARACTERISICS</h2>
      <p>SPECIALTY JAPANESE TOOL STEEL</p>
    </div>
    <div class="abs steel-badge" style="left:42px;top:728px"><span class="dot"></span>Kerova Steel</div>
    <div class="abs steel-badge" style="left:182px;top:728px"><span class="dot"></span>Torunami</div>
    <div class="abs steel-badge" style="left:42px;top:780px"><span class="dot"></span>Belmu Steel</div>
    <div class="abs steel-badge" style="left:182px;top:780px"><span class="dot"></span>Haruvo Steel</div>

    <ul class="abs features">
      <li><span class="ring"></span>PRECISION ENGINEERING</li>
      <li><span class="ring"></span>VACUUM HEAT TREATMENT</li>
      <li><span class="ring"></span>HIGH TOUGHNESS</li>
      <li><span class="ring"></span>HIGH FATIGUE STRENGTH</li>
    </ul>

    <ul class="abs benefits">
      <li>
        <svg width="42" height="42" viewBox="0 0 42 42" aria-hidden="true"><circle cx="21" cy="21" r="19.5" fill="none" stroke="var(--ink)" stroke-width="1.6"/><path d="M14 28v-10M21 28v-14M28 28v-8M11 17l3-3 3 3M18 13l3-3 3 3M25 19l3-3 3 3" fill="none" stroke="var(--ink)" stroke-width="2"/></svg>
        <span><b>IMPROVE</b> TOOL/DIE LIFE</span>
      </li>
      <li>
        <svg width="42" height="42" viewBox="0 0 42 42" aria-hidden="true"><circle cx="21" cy="21" r="19.5" fill="none" stroke="var(--ink)" stroke-width="1.6"/><g fill="var(--ink)"><rect x="12" y="24" width="4" height="5"/><rect x="18" y="20" width="4" height="9"/><rect x="24" y="15" width="4" height="14"/></g><path d="M12 20l12-8" stroke="var(--ink)" stroke-width="1.6"/></svg>
        <span><b>INCREASE</b> PRODUCTIVITY</span>
      </li>
      <li>
        <svg width="42" height="42" viewBox="0 0 42 42" aria-hidden="true"><circle cx="21" cy="21" r="19.5" fill="none" stroke="var(--ink)" stroke-width="1.6"/><text x="21" y="27" text-anchor="middle" font-family="Montserrat,sans-serif" font-weight="700" font-size="16" fill="var(--ink)">$</text><path d="M11 28l4-4M31 28l-4-4" stroke="var(--ink)" stroke-width="2"/></svg>
        <span><b>REDUCE</b> TOOLING COST</span>
      </li>
    </ul>

    <div class="abs company">
      <h3>QORVANE INDUSTRIES</h3>
      <p class="division">A DIVISION OF QORVANE HOLDINGS PTY LTD</p>
      <p class="abn">ABN: 47 203 615 902</p>
    </div>
  </div>
</section>

<section class="sheet sheet--back" aria-label="Flyer back">
  <div class="page">
    <h2 class="abs section-title">PRODUCTS &amp; SERVICES</h2>

    <div class="abs service" style="left:18px"><h4>Extrusion Dies</h4><p>Aluminium, Plastic,<br>Polymers</p></div>
    <div class="abs divider" style="left:185px"></div>
    <div class="abs service" style="left:188px"><h4>Extrusion Dies</h4><p>Aluminium, Steel</p></div>
    <div class="abs divider" style="left:355px"></div>
    <div class="abs service" style="left:359px"><h4>Assorted Tools</h4><p>Precision parts,<br>Punches, Cutters ,<br>dies etc..</p></div>
    <div class="abs divider" style="left:525px"></div>
    <div class="abs service" style="left:528px"><h4>Metallurgical<br>Testings &amp;<br>Verifications</h4></div>

    <div class="abs feature-photo" role="img" aria-label="Photo of an aluminium stamping die with orange springs"></div>
    <svg class="shapes" viewBox="0 0 708 1000" aria-hidden="true">
      <polygon points="344,220 708,220 708,612 266,612" fill="var(--teal)"/>
    </svg>
    <div class="abs caption caption--tall">Stamping Die – Aluminium<br>(photo needs cropping )</div>

    <div class="abs about">
      <h5>Our Reputation</h5>
      <p>Qorvane Industries brings over 20 year of combined experience in Metallurgical R&amp;D, Product Development, Heat Treatment &amp; Tooling Project Management.</p>
      <h5>Who We Are</h5>
      <p>Qorvane Industries is a metallurgical consultant and a supplier of Japanese quality tools, molds and dies.</p>
      <h5>Our Objective</h5>
      <p>Is to work in partnership with you to optimize your tooling performance, reduce tooling cost and to achieve competitive products.</p>
    </div>

    <figure class="abs tile" style="left:32px;top:628px">
      <div class="fill" role="img" aria-label="Photo of customised assorted tools laid out on a bench" style="background:linear-gradient(135deg,#d8d2c8,#8c8780 60%,#b8b1a6)"></div>
      <figcaption class="caption">Customised Assorted Tools (Hot &amp; Cold Applications)</figcaption>
    </figure>
    <figure class="abs tile" style="left:362px;top:628px">
      <div class="fill" role="img" aria-label="Photo of a metallurgical testing instrument examining a steel bar" style="background:linear-gradient(180deg,#e2e2df,#a9a8a2 60%,#8e8a80)"></div>
      <figcaption class="caption">Metallurgical testings &amp; verifications</figcaption>
    </figure>
    <figure class="abs tile" style="left:32px;top:810px">
      <div class="fill" role="img" aria-label="Photo of aluminium extrusion dies" style="background:radial-gradient(ellipse at 50% 55%,#b2b3ad,#8d8f88 55%,#b4b495)"></div>
      <figcaption class="caption">Extrusion Die – Aluminium</figcaption>
    </figure>
    <figure class="abs tile" style="left:362px;top:810px">
      <div class="fill" role="img" aria-label="Photo of a metal stamping die on a blue background" style="background:linear-gradient(180deg,#1f74c4,#3b6f8e 55%,#46675a)"></div>
      <figcaption class="caption">Stamping Die - Metal</figcaption>
    </figure>
  </div>
</section>

</body>
</html>
```